Business card design needed

I need a business card for a new company based in Perth, Western Australia, called KT Power Pty Ltd.

I'm the sole proprietor, and have 25 years' experience in directorship, senior commercial/business development/strategy roles in the oil & gas industry with both supermajors and junior listed companies. I also have interests in renewable energy (and am co-founder and director of a separate renewable energy start-up company). KT Power will be the vehicle for me to contract my services, principally in the oil & gas industry (although this will include directorship services to the renewable energy company). These services will include general consultancy in my areas of expertise, and contracting to provide senior management/director services to start-up or junior oil and gas companies.

I'm looking for a design that communicates professionalism, dynamism, experience, strategic skills and growth.

My ConnectHub profile may also be useful context;

"I have a real passion for discovering new investment opportunities and turning them from talk into reality. Right now my focus is on oil, gas and energy ventures. I’m always on the look out for compelling new investment opportunities where I can bring my leadership and strategic insight to bear to make a real difference by delivering transformational results.

I spent 24 years with HX where I built up extensive international experience in oil, gas and energy and was a member of the company’s “fast track” development programme. As an entrepreneurial senior commercial leader, strategic thinker and tactical dealmaker I was responsible for numerous deals such as divestments, farm-ins, asset swaps, new acreage bids, unitizations, gas and LNG sales, creating billions of dollars of value for HX. These deals frequently broke new ground and/or required an innovative approach that delivered results in excess of what the business thought achievable. I have held senior executive and director roles covering Exploration & Production, Mergers & Acquisitions, Business Development, LNG Marketing, Joint Venture Management, Gas & Power and Corporate head office. International assignments included UK, Australia, Indonesia, Norway & Belgium.

I’m a member of the Guild of Global Fuel Brokers (GGFB) and the Southern Council of Board Members (SCBM).

Board experience comprises four directorships and two alternate directorships of Australian companies, and directorship of a Not for Profit organisation.

Specialties
Strategy, Business Development, Mergers & Acquisitions, Joint Venture Management, Negotiation, Gas & LNG Marketing."

Target Market(s)

Oil and gas or energy companies of all sizes from large listed companies to start-ups - also service providers to the industry.

Industry/Entity Type

Oil And Gas

Contact Information for Business Card

KT Power Pty Ltd
Daniel Hobart
27C Lorne Avenue,
Kelmsdale,
WA 6093

Tel +61 455 823 617
email hobartdk@vellimo.net.au

```html
<!DOCTYPE html>
<html lang="en">
<head>
<meta charset="utf-8">
<title>KT Power Pty Ltd — Business Card</title>
<link rel="stylesheet" href="https://fonts.googleapis.com/css2?family=Federo&family=Gelasio:wght@400&display=swap">
<style>
  :root {
    --card-bg: #ffffff;
    --ink: #111111;
    --ink-soft: #1a1a1a;
  }
  html, body {
    margin: 0;
    padding: 0;
    overflow: hidden;
    background: var(--card-bg);
  }
  .card {
    position: relative;
    width: 1200px;
    height: 651px;
    background: var(--card-bg);
    overflow: hidden;
    color: var(--ink);
  }
  .holder-name {
    position: absolute;
    left: 102px;
    top: 248px;
    margin: 0;
    font-family: "Gelasio", Georgia, serif;
    font-weight: 400;
    font-size: 38px;
    line-height: 46px;
    letter-spacing: 0.3px;
    text-transform: uppercase;
    color: var(--ink);
    white-space: nowrap;
  }
  .brand-mark {
    position: absolute;
    left: 594px;
    top: 152px;
    width: 220px;
    transform: translateX(-50%);
    display: flex;
    flex-direction: column;
    align-items: center;
    gap: 18px;
  }
  .brand-mark__square {
    width: 104px;
    height: 104px;
    background: var(--ink);
  }
  .brand-mark__name {
    margin: 0;
    font-family: "Federo", sans-serif;
    font-weight: 400;
    font-size: 40px;
    line-height: 44px;
    letter-spacing: 2px;
    text-transform: uppercase;
    color: var(--ink);
    white-space: nowrap;
  }
  .company-name {
    position: absolute;
    left: 592px;
    top: 428px;
    transform: translateX(-50%);
    margin: 0;
    font-family: "Federo", sans-serif;
    font-weight: 400;
    font-size: 64px;
    line-height: 68px;
    letter-spacing: 1px;
    text-transform: uppercase;
    color: var(--ink);
    white-space: nowrap;
  }
  .contact {
    position: absolute;
    left: 590px;
    top: 508px;
    transform: translateX(-50%);
    margin: 0;
    font-family: "Gelasio", Georgia, serif;
    font-style: normal;
    font-size: 29px;
    line-height: 35px;
    text-align: center;
    color: var(--ink-soft);
    white-space: nowrap;
  }
  .contact-line {
    display: block;
  }
  .contact-line--upper {
    text-transform: uppercase;
  }
</style>
</head>
<body>
  <main class="card">
    <p class="holder-name">Daniel Hobart</p>
    <div class="brand-mark">
      <div class="brand-mark__square"></div>
      <p class="brand-mark__name">KT Power</p>
    </div>
    <h1 class="company-name">KT Power Pty Ltd.</h1>
    <address class="contact">
      <span class="contact-line contact-line--upper">27C Lorne Avenue, Kelmsdale, WA 6093</span>
      <span class="contact-line">TEL +61 455 823 617</span>
      <span class="contact-line">email hobartdk@vellimo.net.au</span>
    </address>
  </main>
</body>
</html>
```